Natural and organic skincare brand needs label design!

I need labels designed for my natural and organic skincare brand lumavale. The front of the bottles must contain the logo (image attached) and the following words: Formulated by a Naturopath; Anti-aging therapy; Organic Facial Oil; with CoEnzyme Q10 and Rosehip Seed Oil; 100ml e3.38fl.oz. Colours I would like used include black/white/grey/silver and aqua. I also like the grey woodgrain used on my draft website (check out www.lumavale-skin.com.au). The logo should be silver foil (shiny).The final design should be simple and communicate nature and sophistication. Some designs I like are found in the attachments. I intend to use black or white bottles.

Target Market(s)

women aged 30-50 interested in natural products

Industry/Entity Type

Skin Care Product

Font styles to use
Serif
Sans Serif
Decorative
Script
Other font styles liked:
• Any

Requirements
Must have
• Dimensions: 62mm (w) x 75mm (H) (front label only)
• Must contain the logo (image attached). The logo should be silver foil (shiny). and the following words are to be included on the label:
• Formulated by a Naturopath;
• Anti-aging Therapy;
• Organic Facial Oil;
• with CoEnzyme Q10 and Rosehip Seed Oil;
• 100ml e3.38fl.oz.
Nice to have
• Colours I would like used include black/white/grey/silver and aqua (turquoise). But I am also open to suggestion. I also like the grey woodgrain used on my draft website (check out www.lumavale-skin.com.au)

```html
<!DOCTYPE html>
<html lang="en">
<head>
<meta charset="utf-8">
<title>lumavale – Facial Oil Labels</title>
<link rel="stylesheet" href="https://fonts.googleapis.com/css2?family=Marcellus+SC&display=swap">
<style>
  :root {
    --stage-center: #00a3ae;
    --stage-edge: #00838c;
    --label-light: #ffffff;
    --label-dark: #312f31;
    --seal: #525a69;
    --seal-line: #ffffff;
    --ink-dark: #2a2a2a;
    --ink-light: #ffffff;
    --aqua: #2bb5b0;
    --leaf-light-a: #c3c5cc;
    --leaf-light-b: #e6e7ea;
    --leaf-dark-a: #4a505d;
    --leaf-dark-b: #434347;
  }
  * { margin: 0; padding: 0; box-sizing: border-box; }
  html, body { width: 1200px; height: 1200px; overflow: hidden; }
  body {
    background: radial-gradient(ellipse at 50% 50%, var(--stage-center) 0%, var(--stage-edge) 100%);
    font-family: "Marcellus SC", serif;
    position: relative;
  }
  .label {
    position: absolute;
    top: 377px;
    width: 455px;
    height: 549px;
    overflow: hidden;
  }
  .label--white { left: 174px; background: var(--label-light); color: var(--ink-dark); }
  .label--black { left: 644px; background: var(--label-dark); color: var(--ink-light); }

  .foliage {
    position: absolute;
    border-radius: 50%;
    filter: blur(6px);
  }
  .foliage--left { left: -40px; top: 120px; width: 180px; height: 290px; }
  .foliage--right { left: 270px; top: -20px; width: 200px; height: 280px; }
  .label--white .foliage--left { background: radial-gradient(ellipse, var(--leaf-light-a) 0%, rgba(195,197,204,0) 72%); }
  .label--white .foliage--right { background: radial-gradient(ellipse, var(--leaf-light-b) 0%, rgba(230,231,234,0) 72%); }
  .label--black .foliage--left { background: radial-gradient(ellipse, var(--leaf-dark-a) 0%, rgba(74,80,93,0) 72%); }
  .label--black .foliage--right { background: radial-gradient(ellipse, var(--leaf-dark-b) 0%, rgba(67,67,71,0) 72%); }

  .seal {
    position: absolute;
    left: 103px;
    top: 122px;
    width: 248px;
    height: 248px;
    border-radius: 50%;
    background: var(--seal);
    display: flex;
    align-items: center;
    justify-content: center;
  }
  .seal__name {
    color: var(--seal-line);
    font-size: 40px;
    letter-spacing: 4px;
  }

  .copy {
    position: absolute;
    left: 0;
    right: 0;
    top: 407px;
    text-align: center;
    line-height: 1;
  }
  .copy__credit { font-size: 15px; letter-spacing: 0.5px; }
  .copy__title { font-size: 25px; color: var(--aqua); margin-top: 5px; letter-spacing: 0.5px; }
  .copy__product { font-size: 16px; margin-top: 4px; letter-spacing: 0.5px; }
  .copy__actives { font-size: 15px; margin-top: 3px; letter-spacing: 0.8px; }
  .copy__volume { font-size: 14px; margin-top: 14px; }
</style>
</head>
<body>
  <section class="label label--white">
    <div class="foliage foliage--left" role="img" aria-label="Faint grey leafy branch decoration"></div>
    <div class="foliage foliage--right" role="img" aria-label="Pale grey leafy branch decoration"></div>
    <div class="seal"><span class="seal__name">lumavale</span></div>
    <div class="copy">
      <p class="copy__credit">Formulated by a Naturopath</p>
      <h1 class="copy__title">Anti-aging Therapy</h1>
      <p class="copy__product">Organic Facial Oil</p>
      <p class="copy__actives">with CoEnzyme Q10 and Rosehip Seed Oil</p>
      <p class="copy__volume">100ml e3.38fl.oz.</p>
    </div>
  </section>

  <section class="label label--black">
    <div class="foliage foliage--left" role="img" aria-label="Dark slate leafy branch decoration"></div>
    <div class="foliage foliage--right" role="img" aria-label="Charcoal leafy branch decoration"></div>
    <div class="seal"><span class="seal__name">lumavale</span></div>
    <div class="copy">
      <p class="copy__credit">Formulated by a Naturopath</p>
      <h1 class="copy__title">Anti-aging Therapy</h1>
      <p class="copy__product">Organic Facial Oil</p>
      <p class="copy__actives">with CoEnzyme Q10 and Rosehip Seed Oil</p>
      <p class="copy__volume">100ml e3.38fl.oz.</p>
    </div>
  </section>
</body>
</html>
```